Business Card Design for Software Development Company

I am looking for a business card design the incorporates my new logo (attached below).

Key information to include:
Name: Marcus Delvine
Title: CEO
Email: marcus@brightwellcivic.com
Phone: 555-218-4093
Website: www.brightwellcivic.com

NOTE: This design should be easy to edit so that we can order cards for different members of our team.

```html
<!DOCTYPE html>
<html lang="en">
<head>
<meta charset="utf-8">
<title>BrightwellLabs Business Card</title>
<link href="https://fonts.googleapis.com/css2?family=Montserrat:wght@600;700&family=Lato:wght@300;400&display=swap" rel="stylesheet">
<style>
  :root {
    --navy: #373f5b;
    --navy-dark: #2b3149;
    --teal: #16b09c;
    --red: #b3232b;
    --orange: #ee7f24;
    --ink: #2f3652;
    --grey: #6b6e78;
    --paper: #ffffff;
    --backdrop: #1f2023;
  }
  * { margin: 0; padding: 0; box-sizing: border-box; }
  html, body {
    width: 1200px; height: 952px; overflow: hidden;
    background: var(--backdrop);
  }
  .sheet {
    position: relative; width: 1200px; height: 952px;
    display: flex; align-items: center; justify-content: center; gap: 40px;
  }
  .card {
    position: relative; width: 540px; height: 309px;
    overflow: hidden;
    box-shadow: 0 10px 30px rgba(0,0,0,0.45);
  }

  /* Front */
  .card--front { background: var(--paper); }
  .brand {
    position: absolute; left: 38px; top: 112px;
  }
  .brand__name {
    font-family: "Montserrat", sans-serif; font-weight: 700;
    font-size: 27px; letter-spacing: -0.5px; color: var(--ink);
    line-height: 1;
  }
  .brand__tagline {
    font-family: "Montserrat", sans-serif; font-weight: 600;
    font-size: 5.5px; letter-spacing: 0.6px; text-transform: uppercase;
    color: var(--ink); text-align: right; margin-top: 3px;
  }
  .person {
    position: absolute; left: 292px; top: 110px;
  }
  .person__name {
    font-family: "Montserrat", sans-serif; font-weight: 700;
    font-size: 21px; color: var(--ink); line-height: 1.1;
  }
  .person__title {
    font-family: "Lato", sans-serif; font-weight: 300;
    font-size: 13px; color: var(--grey); margin-top: 1px;
  }
  .person__rule {
    width: 48px; height: 1.5px; background: #9a9ca3; margin: 7px 0 10px;
  }
  .contact { list-style: none; }
  .contact__item {
    display: flex; align-items: center; gap: 8px;
    font-family: "Lato", sans-serif; font-weight: 400;
    font-size: 12px; color: var(--grey); margin-bottom: 6px;
  }
  .contact__icon {
    width: 15px; height: 15px; border-radius: 2px;
    display: flex; align-items: center; justify-content: center; flex: none;
  }
  .contact__icon--phone { background: var(--teal); }
  .contact__icon--mail { background: var(--red); }
  .contact__icon--web { background: var(--orange); }
  .edge-band {
    position: absolute; left: 0; bottom: 0; width: 540px; height: 12px;
  }

  /* Back */
  .card--back { background: var(--navy); }
  .back-brand {
    position: absolute; left: 0; right: 0; top: 50%;
    transform: translateY(-50%); text-align: center;
  }
  .back-brand__name {
    font-family: "Montserrat", sans-serif; font-weight: 700;
    font-size: 36px; letter-spacing: -0.5px; color: var(--paper); line-height: 1;
  }
  .back-brand__tagline {
    font-family: "Montserrat", sans-serif; font-weight: 600;
    font-size: 6.5px; letter-spacing: 0.8px; text-transform: uppercase;
    color: var(--paper); margin-top: 5px; padding-left: 150px;
  }
</style>
</head>
<body>
<main class="sheet">

  <section class="card card--front" aria-label="Business card front">
    <div class="brand">
      <div class="brand__name">BrightwellLabs</div>
      <div class="brand__tagline">A Division of Brightwell Civic</div>
    </div>

    <div class="person">
      <h1 class="person__name">Marcus Delvine</h1>
      <p class="person__title">CEO</p>
      <div class="person__rule"></div>
      <ul class="contact">
        <li class="contact__item">
          <span class="contact__icon contact__icon--phone">
            <svg width="9" height="9" viewBox="0 0 24 24" aria-hidden="true"><path fill="#fff" d="M6.6 10.8a15.1 15.1 0 0 0 6.6 6.6l2.2-2.2c.3-.3.7-.4 1-.2 1.1.4 2.3.6 3.6.6.6 0 1 .4 1 1V20c0 .6-.4 1-1 1A17 17 0 0 1 3 4c0-.6.4-1 1-1h3.5c.6 0 1 .4 1 1 0 1.3.2 2.5.6 3.6.1.3 0 .7-.2 1z"/></svg>
          </span>
          555-218-4093
        </li>
        <li class="contact__item">
          <span class="contact__icon contact__icon--mail">
            <svg width="10" height="8" viewBox="0 0 20 14" aria-hidden="true"><rect x="1" y="1" width="18" height="12" fill="none" stroke="#fff" stroke-width="2"/><path d="M1 1l9 7 9-7" fill="none" stroke="#fff" stroke-width="2"/></svg>
          </span>
          marcus@brightwellcivic.com
        </li>
        <li class="contact__item">
          <span class="contact__icon contact__icon--web">
            <svg width="8" height="10" viewBox="0 0 16 20" aria-hidden="true"><path fill="#fff" d="M8 0a7 7 0 0 0-7 7c0 5 7 13 7 13s7-8 7-13a7 7 0 0 0-7-7zm0 9.5A2.5 2.5 0 1 1 8 4.5a2.5 2.5 0 0 1 0 5z"/></svg>
          </span>
          www.brightwellcivic.com
        </li>
      </ul>
    </div>

    <svg class="edge-band" viewBox="0 0 540 12" aria-hidden="true">
      <rect x="0" y="3" width="222" height="4" fill="var(--teal)"/>
      <polygon points="226,3 540,3 540,12 235,12" fill="var(--navy)"/>
    </svg>
  </section>

  <section class="card card--back" aria-label="Business card back">
    <div class="back-brand">
      <div class="back-brand__name">BrightwellLabs</div>
      <div class="back-brand__tagline">A Division of Brightwell Civic</div>
    </div>
  </section>

</main>
</body>
</html>
```